Home Improvement Company in need of a "Banner & Billboard Design"

I'm Looking for a Banner design 4X6 With Company Logo, Phone Number, website, Credentials and services.. I picture a charcoal/matte background i also want to look like a house shape design i will upload the sample...

I'm looking for a Billboard design to target homeowners who need Roofing Services. I need logo, number, website, KTL, Credentials and a catchy title. i will like to use the same colors for branding

Target Market(s)

Homeowners, Investors,

Industry/Entity Type

Home Improvement

Font styles to use
Decorative

Colors
00a990
5c5c5c
333333

Requirements
Must have
• All Credentials, Phone number, website, logo, logo colors, services, Eye Catchy, Direct Message, Friendly feeling,
• (614) 372 - 9058
• Roofing Gutters Painting Pressure Washing Exterior Design
Nice to have
• A catchy title, A direct message to a homeowner looking for home improvement services. noticeable
Should not have
• not Busy, no

```html
<!DOCTYPE html>
<html lang="en">
<head>
<meta charset="utf-8">
<title>Ridgeline Home Exteriors Banner</title>
<link rel="stylesheet" href="https://fonts.googleapis.com/css2?family=Montserrat:wght@300;600;700&display=swap">
<style>
:root{
  --page:#c8c8c8;
  --charcoal-dark:#1b1b1b;
  --charcoal-light:#3b3b3c;
  --teal:#1a9a88;
  --white:#ffffff;
  --ink:#111111;
  --badge:#d4d4d4;
}
*{margin:0;padding:0;box-sizing:border-box}
html,body{width:1200px;height:1000px;overflow:hidden}
body{background:var(--page);position:relative;font-family:"Montserrat",sans-serif}
.banner{
  position:absolute;left:73px;top:148px;width:1054px;height:702px;overflow:hidden;
  background:linear-gradient(90deg,var(--charcoal-dark) 0%,#262626 50%,var(--charcoal-light) 100%);
}
.roof{position:absolute;left:0;top:0;width:1054px;height:702px}
.brand{position:absolute;left:0;right:0;top:270px;text-align:center}
.brand-name{
  font-family:"Montserrat",sans-serif;font-weight:700;color:var(--teal);
  font-size:38px;letter-spacing:1px;line-height:1.1;white-space:nowrap;
}
.brand-name .mark{display:inline-block;width:18px;height:18px;background:var(--teal);margin-right:14px;vertical-align:5px}
.call{
  position:absolute;left:0;right:0;top:424px;text-align:center;
  font-size:74px;line-height:1;white-space:nowrap;
}
.call-label{font-weight:300;color:var(--teal);letter-spacing:2px;margin-right:16px}
.call-number{font-weight:700;color:var(--white)}
.website{
  position:absolute;left:0;right:0;top:516px;text-align:center;
  color:var(--white);font-weight:700;font-size:45px;line-height:1;white-space:nowrap;
}
.website .rule{display:inline-block;width:58px;height:3px;background:var(--white);vertical-align:middle;margin:0 26px}
.credentials-band{
  position:absolute;left:0;bottom:0;width:1054px;height:122px;background:var(--teal);
}
.credentials{position:absolute;left:0;top:18px;width:312px;height:86px}
.badge{position:absolute;top:28px;height:68px;background:var(--badge)}
.badge-listing{left:32px;width:44px}
.badge-certificate{left:88px;width:186px}
.services{
  position:absolute;left:312px;right:0;top:22px;text-align:center;
  color:var(--white);font-weight:600;font-size:30px;line-height:40px;letter-spacing:.5px;white-space:nowrap;
}
.services .sep{display:inline-block;width:12px;height:12px;background:var(--ink);margin:0 10px;vertical-align:4px}
</style>
</head>
<body>
<main class="banner">
  <svg class="roof" viewBox="0 0 1054 702" aria-hidden="true">
    <rect x="905" y="125" width="44" height="80" fill="#1a9a88"/>
    <polygon points="0,247 490,0 560,0 1054,250 1054,292 525,42 0,290" fill="#1a9a88"/>
  </svg>

  <div class="brand">
    <p class="brand-name"><span class="mark"></span>RIDGELINE HOME EXTERIORS</p>
  </div>

  <p class="call"><span class="call-label">CALL</span><span class="call-number">(614) 372 - 9058</span></p>
  <p class="website"><span class="rule"></span>RidgelineHomeExteriors.com<span class="rule"></span></p>

  <section class="credentials-band">
    <svg class="credentials" viewBox="0 0 312 86" aria-hidden="true">
      <polygon points="0,0 292,0 312,43 292,86 0,86" fill="#ffffff"/>
    </svg>
    <div class="badge badge-listing" role="img" aria-label="KTL accreditation badge"></div>
    <div class="badge badge-certificate" role="img" aria-label="Certified roofing contractor badge"></div>
    <p class="services">ROOFING<span class="sep"></span>GUTTERS<span class="sep"></span>PAINTING<br>PRESSURE WASHING<span class="sep"></span>EXTERIOR DESIGN</p>
  </section>
</main>
</body>
</html>
```